New therapy private practice needs a 2 sided postcard announcing location and services

We need a postcard sized card that is TWO SIDED and shares our new location and services offered. (new location is 3842. W. 58th #2300 in Tulsa, OK 74152) Name of the therapy business is "Bright Path! Counseling". Services offered include individual, marriage, family and group counseling. My phone number to place on the card is (918) 555-0143 and someone can call to schedule a free 20 minute consultation at that number.

These cards will also be mailed in an enclosed envelope or placed in welcome baskets as a marketing tool with possible referral sources like churches, doctors, and lawyers. (That means there does not have to be a space for an address or stamp to mail to. Full use of both sides of the card is important) We would like to see designs that use softer colors such as blue, purples, or greens. The final design should communicate a feeling of peace and hope and a sense of freshness and approachability. Incorporating a tag line such as..... "where you'll find hope!" would be good. My website is www.brightpathnow.example and extra info about my practice is on there. It is important my credentials are listed on the postcard. Lena Marsh Voight, LPC-S, LMFT

I am not looking for a bunch of "box looking pictures". The pictures I am uploading are for ideas, although my logo and picture should be used. I like the type of picture I have on my homepage of my website with the quote "Let your hopes, not your fears shape your future"

Target Market(s)

Primarily women and couples looking for counseling for relationships, anxiety, depression, or life transitions.

Font styles to use
Serif
Script

Colors
3276b5
85acd3
86cfc6
33b8a4
cadf82
876aae
9bcb3c

Requirements
Must have
• My picture, address, website, and phone number as well as my logo.
• Address is: 3842 W. 58th Street #2300 Tulsa, OK 74152
• Web: www.brightpathnow.example
• Email: lena@brightpathnow.example
• Phone: (918) 555-0143
• "Hope anchors the soul" - Heb. 6:19
• On my website, I have a 2 minute video of myself. This may be helpful to watch in getting a "feel" for my counseling practice.
• Services Provided: ANXIETY | DEPRESSION | LIFE TRANSITIONS | MARRIAGE COUNSELING | SEPARATION AND DIVORCE | WOMEN’S ISSUES | ADDICTIONS AND INFIDELITY | PARENT/CHILD RELATIONSHIPS | FAMILY CONFLICT | TRAUMA/GRIEF AND LOSS
Nice to have
• A combination of print and script would be nice. A feeling of tranquility and hope
• I would like to have the statement at the bottom of the card.... " It is my desire for you to discover that no matter the situation you are currently going through….. there’s hope!"
• It would also be nice to have a small area that says: Lena is a graduate of Western Calloway College and has been in private practice for 11 years. She is a regular monthly co-host on the Meadow Broadcast Group at 97.3 FM
Should not have
• Heavy bold or abrasive feel

```html
<!DOCTYPE html>
<html lang="en">
<head>
<meta charset="utf-8">
<title>Bright Path! Counseling – Postcard</title>
<link rel="stylesheet" href="https://fonts.googleapis.com/css2?family=Raleway:wght@400;500;700;800&display=swap">
<style>
  :root {
    --stage-dark: #1f3d1c;
    --stage-mid: #3a6a30;
    --white: #ffffff;
    --banner-orange: #fbb040;
    --radio-lime: #cddc39;
    --bullet-yellow: #ffd21f;
    --teal: #14a89a;
    --heading-orange: #f7941d;
    --name-magenta: #e0218a;
    --ink: #222222;
    --icon-green: #39b54a;
    --logo-green: #4a8a2c;
  }
  * { box-sizing: border-box; margin: 0; padding: 0; }
  html, body { width: 1200px; height: 1200px; overflow: hidden; }
  body {
    position: relative;
    font-family: "Raleway", sans-serif;
    background: radial-gradient(circle at 35% 55%, var(--stage-mid) 0%, var(--stage-dark) 80%);
  }
  .card {
    position: absolute;
    overflow: hidden;
    box-shadow: 0 4px 14px rgba(0,0,0,.45);
  }

  /* Front */
  .card--front { left: 70px; top: 83px; width: 704px; height: 509px; }
  .front-photo {
    position: absolute; inset: 0;
    background:
      radial-gradient(ellipse at 10% 20%, rgba(240,220,170,.55) 0%, transparent 40%),
      linear-gradient(180deg, #9aa6ad 0%, #6b6a60 30%, #2f2a20 62%, #17130d 100%);
  }
  .logo-panel {
    position: absolute; left: 94px; top: 0; width: 229px; height: 140px;
    background: var(--white); border-radius: 0 0 8px 8px;
    display: flex; align-items: center; justify-content: center; gap: 10px;
    padding: 0 22px;
  }
  .logo-panel__dot { width: 16px; height: 16px; border-radius: 50%; background: var(--logo-green); flex: none; }
  .logo-panel__name { font-weight: 700; font-size: 19px; line-height: 23px; color: var(--logo-green); }
  .tagline-banner {
    position: absolute; left: 0; top: 166px; width: 530px; height: 45px;
    background: var(--banner-orange); border-radius: 0 23px 23px 0;
    display: flex; align-items: center; padding-left: 38px;
  }
  .tagline-banner__text { color: var(--white); font-weight: 800; font-size: 30px; letter-spacing: .2px; white-space: nowrap; }
  .radio-note {
    position: absolute; left: 42px; top: 216px;
    color: var(--radio-lime); font-size: 16.5px; font-weight: 500; white-space: nowrap;
  }
  .services { position: absolute; left: 45px; top: 256px; list-style: none; }
  .services li {
    display: flex; align-items: center; gap: 5px;
    height: 20.2px; color: var(--white); font-size: 14px; font-weight: 500;
  }
  .services svg { width: 9px; height: 12px; flex: none; }

  /* Back */
  .card--back {
    left: 422px; top: 622px; width: 700px; height: 506px;
    background:
      radial-gradient(ellipse at 95% 5%, rgba(247,130,90,.6) 0%, transparent 30%),
      radial-gradient(ellipse at 55% 18%, rgba(160,215,120,.55) 0%, transparent 40%),
      radial-gradient(ellipse at 85% 85%, rgba(250,225,80,.55) 0%, transparent 45%),
      radial-gradient(ellipse at 5% 95%, rgba(60,190,90,.6) 0%, transparent 35%),
      radial-gradient(ellipse at 2% 30%, rgba(150,215,200,.5) 0%, transparent 30%),
      #fdfdf4;
  }
  .back-photo { position: absolute; left: 42px; width: 224px; }
  .back-photo--top {
    top: 0; height: 203px;
    background: linear-gradient(160deg, #b7c08f 0%, #6f7f4a 50%, #4a5a30 100%);
  }
  .back-photo--bottom {
    top: 231px; height: 224px;
    background: linear-gradient(180deg, #7d8a55 0%, #55683a 45%, #3c5a2a 100%);
  }
  .consult-band {
    position: absolute; left: 0; top: 203px; width: 678px; height: 28px;
    background: var(--teal); border-radius: 0 14px 14px 0;
  }
  .consult-band__text {
    position: absolute; left: 282px; top: 0; line-height: 28px;
    color: var(--white); font-weight: 700; font-size: 23px; white-space: nowrap;
  }
  .consult-lead {
    position: absolute; left: 282px; top: 172px;
    color: var(--heading-orange); font-weight: 700; font-size: 24px; white-space: nowrap;
  }
  .therapist { position: absolute; left: 282px; top: 252px; color: var(--name-magenta); white-space: nowrap; }
  .therapist__name { font-weight: 800; font-size: 26px; line-height: 32px; }
  .therapist__creds { font-weight: 400; font-size: 23px; line-height: 28px; }
  .contact { position: absolute; left: 282px; top: 334px; color: var(--ink); font-size: 15px; z-index: 2; white-space: nowrap; }
  .contact__row { display: flex; align-items: flex-start; gap: 7px; }
  .contact__row svg { width: 14px; height: 16px; flex: none; margin-top: 2px; }
  .contact__row--address { line-height: 22px; margin-bottom: 8px; }
  .contact__row--line { line-height: 23px; }
  .portrait {
    position: absolute; left: 534px; top: 314px; width: 150px; height: 192px;
    border-radius: 75px 75px 0 0;
    background: linear-gradient(180deg, #e8c98a 0%, #d6a57c 40%, #7a1f3a 75%, #5a1428 100%);
  }
</style>
</head>
<body>

<section class="card card--front" aria-label="Postcard front">
  <div class="front-photo" role="img" aria-label="Photo of a woman sitting on a rock ledge overlooking a misty forested canyon at sunrise"></div>
  <div class="logo-panel">
    <span class="logo-panel__dot"></span>
    <span class="logo-panel__name">Bright Path! Counseling</span>
  </div>
  <div class="tagline-banner"><span class="tagline-banner__text">"WHERE YOU'LL FIND HOPE!"</span></div>
  <p class="radio-note">Lena can be heard monthly on the Meadow Broadcast Group at 97.3 FM</p>
  <ul class="services">
    <li><svg viewBox="0 0 9 12"><ellipse cx="4.5" cy="6" rx="3" ry="5.5" transform="rotate(25 4.5 6)" fill="var(--bullet-yellow)"/></svg>ANXIETY</li>
    <li><svg viewBox="0 0 9 12"><ellipse cx="4.5" cy="6" rx="3" ry="5.5" transform="rotate(25 4.5 6)" fill="var(--bullet-yellow)"/></svg>DEPRESSION</li>
    <li><svg viewBox="0 0 9 12"><ellipse cx="4.5" cy="6" rx="3" ry="5.5" transform="rotate(25 4.5 6)" fill="var(--bullet-yellow)"/></svg>LIFE TRANSITIONS</li>
    <li><svg viewBox="0 0 9 12"><ellipse cx="4.5" cy="6" rx="3" ry="5.5" transform="rotate(25 4.5 6)" fill="var(--bullet-yellow)"/></svg>MARRIAGE COUNSELING</li>
    <li><svg viewBox="0 0 9 12"><ellipse cx="4.5" cy="6" rx="3" ry="5.5" transform="rotate(25 4.5 6)" fill="var(--bullet-yellow)"/></svg>SEPARATION AND DIVORCE</li>
    <li><svg viewBox="0 0 9 12"><ellipse cx="4.5" cy="6" rx="3" ry="5.5" transform="rotate(25 4.5 6)" fill="var(--bullet-yellow)"/></svg>WOMEN'S ISSUES</li>
    <li><svg viewBox="0 0 9 12"><ellipse cx="4.5" cy="6" rx="3" ry="5.5" transform="rotate(25 4.5 6)" fill="var(--bullet-yellow)"/></svg>ADDICTIONS AND INFIDELITY</li>
    <li><svg viewBox="0 0 9 12"><ellipse cx="4.5" cy="6" rx="3" ry="5.5" transform="rotate(25 4.5 6)" fill="var(--bullet-yellow)"/></svg>PARENT/CHILD RELATIONSHIPS</li>
    <li><svg viewBox="0 0 9 12"><ellipse cx="4.5" cy="6" rx="3" ry="5.5" transform="rotate(25 4.5 6)" fill="var(--bullet-yellow)"/></svg>FAMILY CONFLICT</li>
    <li><svg viewBox="0 0 9 12"><ellipse cx="4.5" cy="6" rx="3" ry="5.5" transform="rotate(25 4.5 6)" fill="var(--bullet-yellow)"/></svg>TRAUMA/GRIEF AND LOSS</li>
  </ul>
</section>

<section class="card card--back" aria-label="Postcard back">
  <div class="back-photo back-photo--top" role="img" aria-label="Photo of birch trees with yellow autumn leaves falling"></div>
  <div class="back-photo back-photo--bottom" role="img" aria-label="Photo of a joyful woman sitting in a meadow with arms raised among falling leaves"></div>
  <div class="consult-band"><span class="consult-band__text">FREE 20 MINUTE CONSULTATION</span></div>
  <p class="consult-lead">CALL TO SCHEDULE A</p>
  <div class="therapist">
    <p class="therapist__name">LENA MARSH</p>
    <p class="therapist__creds">VOIGHT, LPC-S, LMFT</p>
  </div>
  <div class="portrait" role="img" aria-label="Portrait photo of therapist Lena Marsh Voight"></div>
  <div class="contact">
    <div class="contact__row contact__row--address">
      <svg viewBox="0 0 14 16"><path d="M7 0a5.5 5.5 0 0 0-5.5 5.5C1.5 10 7 16 7 16s5.5-6 5.5-10.5A5.5 5.5 0 0 0 7 0zm0 7.8a2.3 2.3 0 1 1 0-4.6 2.3 2.3 0 0 1 0 4.6z" fill="var(--icon-green)"/></svg>
      <span>3842 W. 58th Street<br>#2300 Tulsa, OK 74152</span>
    </div>
    <div class="contact__row contact__row--line">
      <svg viewBox="0 0 14 16"><path d="M3 1l3 3.5-1.6 2a9 9 0 0 0 4 4.2l2-1.6L14 12l-2 3C6 15 1 9 1 3z" fill="var(--icon-green)"/></svg>
      <span>918.555.0143</span>
    </div>
    <div class="contact__row contact__row--line">
      <svg viewBox="0 0 14 16"><rect x="0.5" y="4" width="13" height="9" fill="none" stroke="var(--icon-green)" stroke-width="1.4"/><path d="M0.5 4l6.5 5 6.5-5" fill="none" stroke="var(--icon-green)" stroke-width="1.4"/></svg>
      <span>lena@brightpathnow.example</span>
    </div>
    <div class="contact__row contact__row--line">
      <svg viewBox="0 0 14 16"><circle cx="7" cy="8" r="6" fill="none" stroke="var(--icon-green)" stroke-width="1.4"/><ellipse cx="7" cy="8" rx="2.6" ry="6" fill="none" stroke="var(--icon-green)" stroke-width="1.2"/><path d="M1 8h12" stroke="var(--icon-green)" stroke-width="1.2"/></svg>
      <span>www.brightpathnow.example</span>
    </div>
  </div>
</section>

</body>
</html>
```